Website for Hash Orbita a cyrpto Mining company that sells crypto mining rigs

β€œIn the age of de-centralised financial services, individuals with a relatively small investment can use their own hardware to process crypto transactions and earn a substantial second income.”

Hash Orbita provide a personal home and hosted mining solutions to enable individuals to earn monthly crypto currencies of today and the future.”
Home/Products/About
Images – I had assumed this was part of the Design? For the home page I have a 10 second video of blockchain. I can only find on Pixelvault For any text or sections please refer to our old website www.thirdheron.ae
https://www.pixelvaultmedia.com/video/clip-2947163058-block-chain-concept---consists-network-connections I can buy and send?
On each page I will have a video similar, can you just put placeholder images and videos. I can replace. I am pretty good with Wordpress.
Updates

Please use text from my old website www.thirdheronmining.com

Target Market(s)

High Net wealth interested in Crypto

Industry/Entity Type

Crypto Mining

Coding

Coded - Design and coding required

Number of Pages Required

5+ page

Font styles to use
Other font styles liked:
• Sansation

Colors
0054AA
0677BA
7BADD7
CADEEF
E8F1F8

Requirements
Must have
• Video as banner (Will supply Video), Wordpress
Nice to have
• Will need Member login and Shop in future, please ensure this will be possible. (But not part of this project)

```html
<!DOCTYPE html>
<html lang="en">
<head>
<meta charset="utf-8">
<title>Hash Orbita – Services</title>
<link href="https://fonts.googleapis.com/css2?family=Exo+2:wght@400;500;600&display=swap" rel="stylesheet">
<style>
:root{
  --ink:#000000;
  --deep:#050a10;
  --blue:#0054AA;
  --mid:#0677BA;
  --bright:#0aa4e8;
  --sky:#7BADD7;
  --pale:#CADEEF;
  --mist:#E8F1F8;
  --white:#ffffff;
  --text:#e9eef3;
}
*{margin:0;padding:0;box-sizing:border-box}
html,body{width:1200px;height:4158px;overflow:hidden}
body{position:relative;background:radial-gradient(ellipse at 50% 30%,#0d1620 0%,#05080c 55%,#000 100%);font-family:"Exo 2",sans-serif;color:var(--text)}
.abs{position:absolute}
.hero-shape{position:absolute;left:0;top:0;width:1200px;height:450px}
.logo{position:absolute;left:97px;top:18px;display:flex;align-items:center;gap:12px;font-size:32px;font-weight:500;letter-spacing:2px;color:var(--bright)}
.logo-mark{width:30px;height:30px;border:3px solid var(--bright);border-radius:50%}
.nav{position:absolute;top:33px;left:493px;display:flex;gap:0;font-size:15px;color:var(--white)}
.nav a{color:inherit;text-decoration:none;position:absolute;white-space:nowrap}
.nav a.active{color:var(--bright)}
.login{position:absolute;left:969px;top:21px;width:131px;height:44px;background:var(--bright);border-radius:3px;color:#fff;font-size:15px;font-weight:600;display:flex;align-items:center;justify-content:center;gap:6px}
.hero-title{position:absolute;top:262px;left:0;width:1200px;text-align:center;font-size:64px;font-weight:400;color:#fff;letter-spacing:1px}
.card{position:absolute;width:499px;height:348px;border:2px solid var(--bright);border-radius:6px;background:linear-gradient(180deg,rgba(0,0,0,.85),rgba(8,16,24,.8))}
.card.left{left:100px}
.card.right{left:599px}
.card h2{position:absolute;top:36px;font-size:27px;font-weight:600;color:#fff}
.card.left h2{left:21px}
.card.right h2{left:91px}
.card p{position:absolute;top:78px;font-size:12.6px;line-height:24.4px;text-align:justify;color:var(--text)}
.card.left p{left:24px;width:382px}
.card.right p{left:93px;width:382px}
.badge{position:absolute;left:555px;width:88px;height:88px;border-radius:50%;background:var(--bright);box-shadow:0 0 0 4px rgba(10,164,232,.25);display:flex;align-items:center;justify-content:center}
.contact-band{position:absolute;left:0;top:3020px;width:1200px;height:715px}
.contact-title{position:absolute;top:3192px;left:0;width:1200px;text-align:center;font-size:36px;font-weight:600;color:#fff}
.field{position:absolute;background:#fff;color:#777;font-size:14px;padding:20px 18px}
.submit{position:absolute;left:505px;top:3530px;width:189px;height:44px;border:2px solid #fff;border-radius:22px;color:#fff;font-size:14px;display:flex;align-items:center;justify-content:center}
.foot-head{position:absolute;top:3832px;font-size:17px;font-weight:600;color:#fff}
.foot-item{position:absolute;font-size:15px;line-height:20px;color:#fff}
.foot-icon{position:absolute}
.links a{display:block;color:#fff;text-decoration:none;font-size:15px;line-height:27px}
.news-input{position:absolute;left:693px;top:3883px;width:225px;height:45px;background:#fff;color:#666;font-size:13px;padding:14px 16px}
.news-btn{position:absolute;left:918px;top:3883px;width:138px;height:45px;background:var(--bright);color:#fff;font-size:15px;font-weight:600;display:flex;align-items:center;justify-content:center}
.social{position:absolute;top:3959px;width:38px;height:38px;border:2px solid var(--bright);border-radius:50%}
.social::after{content:"";position:absolute;left:12px;top:12px;width:10px;height:10px;border-radius:50%;background:var(--bright)}
.copyright{position:absolute;top:4110px;left:0;width:1200px;text-align:center;font-size:15px;color:#fff}
</style>
</head>
<body>

<svg class="hero-shape" viewBox="0 0 1200 450" role="img" aria-label="Banner video placeholder: glowing blockchain circuitry with a floating crystal coin">
  <defs>
    <linearGradient id="heroFill" x1="0" y1="0" x2="1" y2="1">
      <stop offset="0" stop-color="#0c2a33"/>
      <stop offset=".5" stop-color="#123f48"/>
      <stop offset="1" stop-color="#3a1e0e"/>
    </linearGradient>
  </defs>
  <path d="M0 0H1200V291L905 440L598 358L290 440L0 291Z" fill="url(#heroFill)"/>
  <path d="M0 291L290 440L598 358L905 440L1200 291" fill="none" stroke="#0aa4e8" stroke-width="4"/>
</svg>

<div class="logo"><span class="logo-mark"></span>Hash Orbita</div>
<nav class="nav">
  <a style="left:0">Home</a>
  <a style="left:76px">Services</a>
  <a style="left:166px">Product</a>
  <a style="left:252px">About</a>
  <a class="active" style="left:326px">FAQ</a>
  <a style="left:389px">Contact</a>
</nav>
<div class="login">
  <svg width="12" height="13" viewBox="0 0 12 13"><circle cx="6" cy="3.5" r="3" fill="#fff"/><path d="M0 13c0-4 2.5-6 6-6s6 2 6 6z" fill="#fff"/></svg>LOGIN
</div>
<h1 class="hero-title">SERVICES</h1>

<!-- Service cards -->
<section class="card left" style="top:557px">
  <h2>Hardware Installation</h2>
  <p>In the last few years, the cost of technology required to 'mine' crypto has fallen significantly and the speed and ability has rocketed. Our team acquire the latest technology and build you a custom mining rig for you based on your investment criteria. The rig runs itself, you don't need to do anything. Your Rig then earns you crypto every day.</p>
</section>
<div class="badge" style="top:689px"><svg width="44" height="44" viewBox="0 0 44 44" fill="none" stroke="#fff" stroke-width="2"><rect x="11" y="11" width="22" height="22"/><rect x="17" y="17" width="10" height="10"/><path d="M16 4v7M22 4v7M28 4v7M16 33v7M22 33v7M28 33v7M4 16h7M4 22h7M4 28h7M33 16h7M33 22h7M33 28h7"/></svg></div>

<section class="card right" style="top:953px">
  <h2>Currency Mining</h2>
  <p>Our typical "Onyx" rig contains 6 high powered gaming cards (GPUs) that produce amazing processing capability. This home mining rig costs just 48,600 AED for full home installation and typically earns up to 0.4 ETH per month, for a minimum of 48 months.<br>We buy the hardware through our wholesale contacts, manufacturers and distrobutors.<br>We add 10% margin with complete transparency to show you the cost paid for the hardware.</p>
</section>
<div class="badge" style="top:1085px"><svg width="44" height="44" viewBox="0 0 44 44" fill="none" stroke="#fff" stroke-width="2"><path d="M6 10c8-6 18-4 24 2M18 8l-8 26"/><circle cx="28" cy="30" r="9"/><path d="M24 30h8M28 26v8"/></svg></div>

<section class="card left" style="top:1349px">
  <h2>Crypto Earnings</h2>
  <p>With 48,600 AED invested, the Third Heron rig returns up to 0.4 ETH per month.<br>So if you buy ETH today you could buy 4 coins, and in four years you would have 4 coins. If you invest in a rig, you will earn between 0.3 and 0.4 ETH per month, meaning in 48 months you will have accrued up to 14-19 ETH coins.<br>In the medium term it's so much better to mine crypto, as opposed to buy and hold.</p>
</section>
<div class="badge" style="top:1481px"><svg width="46" height="46" viewBox="0 0 46 46" fill="none" stroke="#fff" stroke-width="2"><circle cx="23" cy="23" r="9"/><path d="M23 14V4M23 32v10M14 23H4M32 23h10M16 16l-7-7M30 30l7 7M30 16l7-7M16 30l-7 7"/><circle cx="23" cy="4" r="2"/><circle cx="23" cy="42" r="2"/><circle cx="4" cy="23" r="2"/><circle cx="42" cy="23" r="2"/></svg></div>

<section class="card right" style="top:1744px">
  <h2>Earn Crypto Every Month</h2>
  <p>When you become a Third Heron mining member, we help you open a CoinHarbor or LedgerPeak Crypto account for free. Third Heron transfer 90% of your earned crypto into your account on the 1st of every month. You can choose to store it or cash it out to your bank account. It's better to earn crypto than to buy it. Whether the price is rising or dropping, you will earn crypto every month increasing the value of your portfolio. Everyone agrees ETH will be worth significantly more by 2024, than it is now so to earn ETH gradually is the best medium to long term cryptocurrency strategy.</p>
</section>
<div class="badge" style="top:1876px"><svg width="44" height="44" viewBox="0 0 44 44" fill="none" stroke="#fff" stroke-width="2"><rect x="5" y="8" width="32" height="28" rx="2"/><path d="M5 15h32M12 4v8M30 4v8"/><path d="M11 21h3M18 21h3M25 21h3M11 27h3M18 27h3"/><circle cx="33" cy="33" r="7" fill="#0aa4e8"/><path d="M30 33l2 2 4-4"/></svg></div>

<section class="card left" style="top:2138px">
  <h2>Service &amp; Maintenance</h2>
  <p>The Third Heron service and maintenance team guarantee 96% platform up time, 24/7 customer service and same day call out if any issues cannot be resolved virtually. Our teams are based in Dubai, but also around the world ensuring 24/7 support.<br>This is the 10% of your Monthly Crypto earnings charged by Third Heron, whereas the 90% of your crypto earnings are automatically swept and sent to you on the 1st of every month.</p>
</section>
<div class="badge" style="top:2270px"><svg width="46" height="46" viewBox="0 0 46 46" fill="none" stroke="#fff" stroke-width="2"><path d="M23 5l4 5 6-2 1 6 6 2-2 6 4 4-4 4 2 6-6 2-1 6-6-2-4 5-4-5-6 2-1-6-6-2 2-6-4-4 4-4-2-6 6-2 1-6 6 2z"/><path d="M17 16l12 14M29 16l-12 14"/></svg></div>

<section class="card right" style="top:2534px">
  <h2>Flexible Mining</h2>
  <p>Our Rig design means that you can choose to mine any cryptocurrency, not just Ethereum. Depending on your risk profile, you can choose to mine one of the up and coming Alt Coins that are predicted to become mainstream. There are multiple websites, such as minecalc.io, that show the highest monthly return per crypto currency. ETH is top. However, if ETH changes or you want to be more speculative then switching what your Rig will mine takes less than an hour and can be done remotely. Your Rig is flexible and you can choose what crypto you mine.</p>
</section>
<div class="badge" style="top:2666px"><svg width="44" height="44" viewBox="0 0 44 44" fill="none" stroke="#fff" stroke-width="2"><circle cx="20" cy="24" r="11"/><circle cx="20" cy="24" r="6"/><path d="M28 6a14 14 0 0 1 10 10M34 16l4 0 0-4M6 34l8 6"/></svg></div>

<!-- Get in touch -->
<svg class="contact-band" viewBox="0 3020 1200 715" role="img" aria-label="Contact band background: blue glowing hexagon mesh">
  <defs>
    <linearGradient id="bandFill" x1="0" y1="0" x2="0" y2="1">
      <stop offset="0" stop-color="#0a8fd0"/>
      <stop offset=".55" stop-color="#0677BA"/>
      <stop offset="1" stop-color="#0a8fd0"/>
    </linearGradient>
  </defs>
  <path d="M0 3173L290 3028L598 3109L905 3028L1200 3173V3585L905 3731L598 3647L290 3731L0 3585Z" fill="url(#bandFill)"/>
</svg>
<h2 class="contact-title">GET IN TOUCH</h2>
<div class="field" style="left:266px;top:3262px;width:328px;height:54px">First Name</div>
<div class="field" style="left:604px;top:3262px;width:329px;height:54px">Last Name</div>
<div class="field" style="left:266px;top:3328px;width:328px;height:54px">Phone</div>
<div class="field" style="left:604px;top:3328px;width:329px;height:54px">Email</div>
<div class="field" style="left:266px;top:3395px;width:667px;height:114px">Message</div>
<div class="submit">SUBMIT</div>

<!-- Footer -->
<h3 class="foot-head" style="left:142px">CONTACT US</h3>
<svg class="foot-icon" style="left:146px;top:3882px" width="16" height="22" viewBox="0 0 16 22"><path d="M8 0a8 8 0 0 1 8 8c0 6-8 14-8 14S0 14 0 8a8 8 0 0 1 8-8z" fill="#0aa4e8"/><circle cx="8" cy="8" r="3" fill="#000"/></svg>
<div class="foot-item" style="left:179px;top:3880px;line-height:22px">Hash Orbita<br>195 enim ipsam<br>volatem quia voluptas</div>
<svg class="foot-icon" style="left:145px;top:3954px" width="18" height="18" viewBox="0 0 18 18"><path d="M4 0l4 4-2 3c1 2 3 4 5 5l3-2 4 4-3 4C7 18 0 11 0 3z" fill="#0aa4e8"/></svg>
<div class="foot-item" style="left:179px;top:3952px">Phone:<br>808-4100 5500</div>
<svg class="foot-icon" style="left:145px;top:4018px" width="18" height="13" viewBox="0 0 18 13"><rect width="18" height="13" rx="1" fill="#0aa4e8"/><path d="M0 1l9 6 9-6" fill="none" stroke="#000" stroke-width="1.5"/></svg>
<div class="foot-item" style="left:179px;top:4008px">Email:<br>info@hashorbita.ae</div>

<h3 class="foot-head" style="left:476px">QUICK LINKS</h3>
<nav class="links abs" style="left:481px;top:3868px">
  <a>Home</a><a>Services</a><a style="padding-left:5px">Product</a><a>About</a><a>FAQ</a><a>Contact</a>
</nav>

<h3 class="foot-head" style="left:693px">SIGN UP FOR NEWSLETTER</h3>
<div class="news-input">Email *</div>
<div class="news-btn">SUBMIT</div>
<span class="social" style="left:866px"></span>
<span class="social" style="left:916px"></span>
<span class="social" style="left:966px"></span>
<span class="social" style="left:1016px"></span>

<p class="copyright">Hash Orbita© 2021 All Rights Reserved | Privacy Policy | Terms and Conditions</p>

</body>
</html>
```